School Wide Powerpoint design

We are looking to have a powerpoint template created that can be used across the organization for presentation. It must be in brand (see guidelines attached)

Target Market(s)

Board meetings, prospective families, donors, school community

Colors

Designer to choose colors to be used in the design.

Requirements
Must have
• In brand (Fonts \ colors)

```html
<!DOCTYPE html>
<html lang="en">
<head>
<meta charset="utf-8">
<title>Linden Grove School – Presentation Template</title>
<link rel="stylesheet" href="https://fonts.googleapis.com/css2?family=Lato:wght@400;700;900&display=swap">
<style>
:root{
  --navy:#1f3a5c;
  --yellow:#e3c23b;
  --green:#2e7a4b;
  --red:#c9452f;
  --grey:#ebebeb;
  --ink:#3a3a3a;
  --muted:#8a8a8a;
  --white:#ffffff;
  --bg-top:#f5d5ca;
  --bg-bottom:#f2e6dc;
}
*{box-sizing:border-box;margin:0;padding:0}
html,body{width:1200px;height:2200px;overflow:hidden}
body{
  position:relative;
  font-family:"Lato",Arial,sans-serif;
  color:var(--ink);
  background:linear-gradient(180deg,var(--bg-top) 0%,var(--bg-bottom) 100%);
}
.slide{
  position:absolute;width:552px;height:310px;overflow:hidden;
  background:var(--white);
  box-shadow:0 6px 18px rgba(60,30,20,.22);
}
.col-left{left:36px}
.col-right{left:612px}
.row-1{top:470px}.row-2{top:820px}.row-3{top:1170px}.row-4{top:1520px}.row-5{top:1870px}
.photo{position:absolute}
.shape{position:absolute;inset:0;width:100%;height:100%}
.brand{
  position:absolute;display:flex;align-items:center;gap:8px;
  font-family:"Lato",Arial,sans-serif;font-weight:700;color:var(--navy);
  font-size:15px;letter-spacing:.5px;line-height:1.1;
}
.brand-dot{width:10px;height:10px;border-radius:50%;background:var(--navy);flex:none}
.brand.light{color:var(--white)}
.brand.light .brand-dot{background:var(--white)}
.page-no{position:absolute;right:14px;bottom:8px;font-size:9px;color:var(--muted)}

/* hero slide */
.hero{position:absolute;left:40px;top:24px;width:620px;height:349px;box-shadow:0 10px 26px rgba(60,30,20,.3)}
.hero .brand{left:28px;top:48px;font-size:22px}
.hero .brand-dot{width:14px;height:14px}

/* feature list */
.features{position:absolute;left:708px;top:28px;width:470px;list-style:none;font-size:21px;line-height:1.45;color:#222}
.features li{padding-left:26px;position:relative}
.features li::before{content:"";position:absolute;left:0;top:8px;width:14px;height:14px;border:1.5px solid #333}
.features ul{list-style:none;margin-left:30px;font-size:19px}
.features ul li{padding-left:18px}
.features ul li::before{border:none;width:7px;height:7px;background:#333;border-radius:50%;top:11px}

/* slide type */
.tagline{position:absolute;color:var(--white);font-weight:700;font-size:17px;line-height:1.25}
.slide-title{position:absolute;font-weight:400;font-size:19px;color:var(--ink)}
.body-copy{position:absolute;font-size:7.5px;line-height:1.5;color:var(--muted)}
.body-copy p+p{margin-top:7px}
.band-title{position:absolute;color:var(--white);font-size:13px;font-weight:700;padding:6px 14px;background:var(--navy)}
.agenda{position:absolute;left:22px;top:30px;color:var(--white)}
.agenda h3{font-size:16px;margin-bottom:10px}
.agenda li{list-style:none;font-size:10px;margin-bottom:8px;padding-left:12px;position:relative}
.agenda li::before{content:"";position:absolute;left:0;top:4px;width:5px;height:5px;background:var(--yellow)}
.caption{position:absolute;font-size:9px;color:var(--white)}

.pillars{position:absolute;left:40px;top:100px;width:472px;display:flex;justify-content:space-between}
.pillar{width:130px;text-align:center;color:var(--white)}
.pillar-icon{width:54px;height:54px;margin:0 auto 12px;border-radius:50%;background:var(--yellow);display:flex;align-items:center;justify-content:center}
.pillar h4{font-size:10px;margin-bottom:5px;color:var(--yellow)}
.pillar p{font-size:7.5px;line-height:1.5;color:#c9d3df}

.stats{position:absolute;left:26px;top:26px;width:500px;display:grid;grid-template-columns:repeat(4,1fr);row-gap:34px}
.stat{display:flex;gap:8px;align-items:flex-start}
.stat-icon{width:14px;height:14px;background:var(--yellow);border-radius:3px;margin-top:5px;flex:none}
.stat b{display:block;font-size:22px;font-weight:900;color:var(--navy);line-height:1}
.stat span{font-size:7.5px;color:var(--muted)}
.stat-note{position:absolute;left:26px;bottom:26px;font-size:8px;color:var(--red)}

.portfolio{position:absolute;left:30px;top:62px;width:492px;height:210px;display:grid;grid-template-columns:repeat(5,1fr);grid-template-rows:1fr 1fr;gap:5px}
.tile{position:relative}

.pies{position:absolute;left:300px;top:70px;display:flex;gap:30px}
.pie{text-align:center;font-size:8px;color:var(--muted)}
.pie svg{display:block;margin-bottom:8px}
</style>
</head>
<body>

<!-- Hero title slide -->
<section class="hero slide" style="width:620px;height:349px">
  <div class="photo" role="img" aria-label="Photo of two smiling students in a classroom" style="inset:0;background:linear-gradient(135deg,#6f5a48 0%,#a88d74 45%,#3f4d5c 100%)"></div>
  <svg class="shape" viewBox="0 0 620 349" preserveAspectRatio="none" aria-hidden="true">
    <polygon points="0,0 250,0 150,349 0,349" fill="#ffffff"/>
    <polygon points="0,200 190,165 150,349 0,349" fill="#e3c23b"/>
  </svg>
  <div class="brand"><span class="brand-dot"></span>LINDEN GROVE<br>SCHOOL</div>
</section>

<ul class="features">
  <li>Ratio 16:9</li>
  <li>Full HD</li>
  <li>Custom color pallet</li>
  <li>Custom Font – Easy Change</li>
  <li>Easy to edit, just drag and drop images</li>
  <li>Can be included up to 50 slides:
    <ul>
      <li>Text + images (1,2,3,4) Text Slides</li>
      <li>Portfolio Slides , blog slides</li>
      <li>Text Slides, infographics</li>
      <li>Data Slides</li>
    </ul>
  </li>
  <li>Its the sample you find 13 slides</li>
</ul>

<!-- 1 Title -->
<section class="slide col-left row-1">
  <div class="photo" role="img" aria-label="Photo of students running on the school playground" style="inset:0;background:linear-gradient(120deg,#8a7c6a,#b3a48a 50%,#5c6a58)"></div>
  <svg class="shape" viewBox="0 0 552 310" preserveAspectRatio="none" aria-hidden="true">
    <polygon points="0,0 210,0 160,120 0,120" fill="#ffffff"/>
    <polygon points="0,120 160,120 130,310 0,310" fill="#e3c23b"/>
  </svg>
  <div class="brand" style="left:18px;top:40px"><span class="brand-dot"></span>LINDEN GROVE<br>SCHOOL</div>
  <div class="tagline" style="left:18px;top:160px;width:120px">We can change everything together</div>
</section>

<!-- 2 Mission -->
<section class="slide col-right row-1">
  <div class="photo" role="img" aria-label="Photo of families sitting on the lawn outside the school" style="left:0;top:0;width:230px;height:310px;background:linear-gradient(150deg,#7fa06a,#c7c0a5 60%,#8a9a7a)"></div>
  <svg class="shape" viewBox="0 0 552 310" preserveAspectRatio="none" aria-hidden="true">
    <polygon points="0,250 80,310 0,310" fill="#e3c23b"/>
    <rect x="230" y="34" width="322" height="36" fill="#ebebeb"/>
  </svg>
  <div class="slide-title" style="left:340px;top:40px">Our Mission</div>
  <div class="body-copy" style="left:252px;top:90px;width:280px">
    <p>Our school brings students, families and teachers together to learn with curiosity, care and respect. Each day we build a place where every voice is heard.</p>
    <p>We believe learning grows through questions, service and friendship. Students explore ideas in class, outdoors and across our wider community with open minds.</p>
    <p>Together we prepare young people to think clearly, act kindly and lead with purpose in a changing world.</p>
  </div>
  <span class="page-no">2</span>
</section>

<!-- 3 Title band -->
<section class="slide col-left row-2">
  <div class="photo" role="img" aria-label="Photo of students and teachers playing on the school field" style="inset:0;background:linear-gradient(160deg,#6d8f5a,#a9b98a 50%,#6a7a52)"></div>
  <div class="band-title" style="left:0;top:22px">Your title here</div>
  <svg class="shape" viewBox="0 0 552 310" preserveAspectRatio="none" aria-hidden="true">
    <rect x="0" y="215" width="552" height="30" fill="#e3c23b"/>
    <polygon points="380,245 552,190 552,310 360,310" fill="#2e7a4b"/>
  </svg>
  <div class="caption" style="left:18px;top:224px;color:var(--navy)">Add a short subtitle to this slide</div>
  <div class="brand light" style="left:410px;top:262px;font-size:12px"><span class="brand-dot"></span>LINDEN GROVE<br>SCHOOL</div>
</section>

<!-- 4 Photo with diagonals -->
<section class="slide col-right row-2">
  <div class="photo" role="img" aria-label="Photo of students in uniform outside under autumn trees" style="inset:0;background:linear-gradient(130deg,#7a8fa6,#b79c6c 55%,#7b6a4e)"></div>
  <svg class="shape" viewBox="0 0 552 310" preserveAspectRatio="none" aria-hidden="true">
    <polygon points="430,0 552,0 552,310 340,310" fill="#e3c23b" opacity=".9"/>
    <polygon points="490,0 552,0 552,310 430,310" fill="#c9452f" opacity=".95"/>
  </svg>
</section>

<!-- 5 Agenda -->
<section class="slide col-left row-3">
  <div class="photo" role="img" aria-label="Photo of two young students working at a classroom table" style="left:190px;top:0;width:362px;height:310px;background:linear-gradient(140deg,#a89078,#d0bfa2 50%,#6f7c8a)"></div>
  <svg class="shape" viewBox="0 0 552 310" preserveAspectRatio="none" aria-hidden="true">
    <polygon points="0,0 220,0 190,310 0,310" fill="#c9452f"/>
    <rect x="0" y="280" width="200" height="8" fill="#e3c23b"/>
  </svg>
  <div class="agenda">
    <h3>Agenda</h3>
    <ul>
      <li>Welcome and introductions</li>
      <li>Year in review</li>
      <li>Campus plans</li>
      <li>Questions</li>
    </ul>
  </div>
</section>

<!-- 6 Stripes -->
<section class="slide col-right row-3">
  <div class="photo" role="img" aria-label="Photo of smiling students in the school garden" style="inset:0;background:linear-gradient(120deg,#5e7a4a,#9bb07a 50%,#4f6a40)"></div>
  <svg class="shape" viewBox="0 0 552 310" preserveAspectRatio="none" aria-hidden="true">
    <rect x="0" y="126" width="240" height="18" fill="#e3c23b"/>
    <rect x="0" y="144" width="240" height="18" fill="#c9452f"/>
    <rect x="0" y="162" width="240" height="18" fill="#2e7a4b"/>
    <rect x="0" y="230" width="200" height="80" fill="#ffffff"/>
  </svg>
  <div class="caption" style="left:14px;top:130px;color:var(--navy)">Add your caption here</div>
  <div class="brand" style="left:16px;top:252px;font-size:13px"><span class="brand-dot"></span>LINDEN GROVE<br>SCHOOL</div>
</section>

<!-- 7 Pillars -->
<section class="slide col-left row-4" style="background:var(--navy)">
  <div class="brand light" style="left:22px;top:22px;font-size:13px"><span class="brand-dot"></span>LINDEN GROVE<br>SCHOOL</div>
  <div class="pillars">
    <div class="pillar">
      <div class="pillar-icon"><svg width="24" height="24" viewBox="0 0 24 24" aria-hidden="true"><path d="M5 12l5 5 9-10" fill="none" stroke="#1f3a5c" stroke-width="3"/></svg></div>
      <h4>Your text</h4>
      <p>Share one key idea for this section here.</p>
    </div>
    <div class="pillar">
      <div class="pillar-icon"><svg width="24" height="24" viewBox="0 0 24 24" aria-hidden="true"><path d="M5 12l5 5 9-10" fill="none" stroke="#1f3a5c" stroke-width="3"/></svg></div>
      <h4>Your text</h4>
      <p>Share one key idea for this section here.</p>
    </div>
    <div class="pillar">
      <div class="pillar-icon"><svg width="24" height="24" viewBox="0 0 24 24" aria-hidden="true"><path d="M5 12l5 5 9-10" fill="none" stroke="#1f3a5c" stroke-width="3"/></svg></div>
      <h4>Your text</h4>
      <p>Share one key idea for this section here.</p>
    </div>
  </div>
  <span class="page-no" style="color:#9fb0c4">7</span>
</section>

<!-- 8 Stats -->
<section class="slide col-right row-4">
  <div class="stats">
    <div class="stat"><i class="stat-icon"></i><div><b>77</b><span>acres of campus</span></div></div>
    <div class="stat"><i class="stat-icon"></i><div><b>8-9</b><span>average class size</span></div></div>
    <div class="stat"><i class="stat-icon"></i><div><b>10:1</b><span>student teacher ratio</span></div></div>
    <div class="stat"><i class="stat-icon"></i><div><b>5</b><span>languages offered</span></div></div>
    <div class="stat"><i class="stat-icon"></i><div><b>20</b><span>clubs and teams</span></div></div>
    <div class="stat"><i class="stat-icon"></i><div><b>11</b><span>years of service</span></div></div>
  </div>
  <div role="img" aria-label="Decorative leaf illustration" style="position:absolute;right:40px;top:150px;width:80px;height:80px;border-radius:50%;background:var(--ink)"></div>
  <div class="stat-note">Add a short summary line here</div>
  <span class="page-no">8</span>
</section>

<!-- 9 Portfolio -->
<section class="slide col-left row-5">
  <div class="brand" style="left:22px;top:18px;font-size:11px"><span class="brand-dot" style="width:8px;height:8px"></span>LINDEN GROVE<br>SCHOOL</div>
  <div class="slide-title" style="left:210px;top:22px;font-size:16px">Portfolio Images</div>
  <div class="portfolio">
    <div class="tile" style="background:var(--green)"></div>
    <div class="tile photo" role="img" aria-label="Photo of students in class" style="position:relative;background:linear-gradient(135deg,#8a7a66,#b8a58a)"></div>
    <div class="tile" style="background:var(--navy)"></div>
    <div class="tile photo" role="img" aria-label="Photo of students outdoors" style="position:relative;background:linear-gradient(135deg,#6c8a58,#a6b88a)"></div>
    <div class="tile" style="background:var(--yellow)"></div>
    <div class="tile photo" role="img" aria-label="Photo of a teacher with students" style="position:relative;background:linear-gradient(135deg,#7a6a5a,#a89478)"></div>
    <div class="tile" style="background:var(--red)"></div>
    <div class="tile photo" role="img" aria-label="Photo of the school building" style="position:relative;background:linear-gradient(135deg,#7d8c9c,#b4b0a2)"></div>
    <div class="tile" style="background:var(--green)"></div>
    <div class="tile photo" role="img" aria-label="Photo of students at an event" style="position:relative;background:linear-gradient(135deg,#9a7f64,#c8b08e)"></div>
  </div>
  <span class="page-no">9</span>
</section>

<!-- 10 Statistics -->
<section class="slide col-right row-5">
  <div class="photo" role="img" aria-label="Photo of students playing basketball in the gym" style="left:0;top:0;width:270px;height:310px;background:linear-gradient(150deg,#8c6e52,#b6906a 50%,#5a5048)"></div>
  <svg class="shape" viewBox="0 0 552 310" preserveAspectRatio="none" aria-hidden="true">
    <rect x="270" y="0" width="282" height="310" fill="#1f3a5c"/>
    <rect x="270" y="20" width="282" height="32" fill="#ebebeb"/>
  </svg>
  <div class="slide-title" style="left:370px;top:25px;font-size:15px">Our Statistics</div>
  <div class="pies">
    <div class="pie" style="color:#c9d3df">
      <svg width="100" height="100" viewBox="0 0 32 32" aria-hidden="true">
        <circle r="16" cx="16" cy="16" fill="#ebebeb"/>
        <circle r="8" cx="16" cy="16" fill="none" stroke="#e3c23b" stroke-width="16" stroke-dasharray="32 50.3" transform="rotate(-90 16 16)"/>
      </svg>
      Lower School
    </div>
    <div class="pie" style="color:#c9d3df">
      <svg width="100" height="100" viewBox="0 0 32 32" aria-hidden="true">
        <circle r="16" cx="16" cy="16" fill="#ebebeb"/>
        <circle r="8" cx="16" cy="16" fill="none" stroke="#2b527f" stroke-width="16" stroke-dasharray="38 50.3" transform="rotate(-90 16 16)"/>
      </svg>
      Upper School
    </div>
  </div>
  <span class="page-no" style="color:#9fb0c4">10</span>
</section>

</body>
</html>
```